Web site for new fundraising service for charities

We need a web design for a new charitable trust based in New Zealand. With the economic downturn, charities are finding it increasingly difficult to raise the monies they need to deliver their services.

Using a network of fundraisers working out of their homes, BrightLot (our charitable trust) will source unique, high interest auction items on behalf of multiple charities - things like luxury cruises, exotic travel, luxury accommodation, fine dining, unique experiences with sports and entertainment personalities, tickets to sporting and entertainment events, etc.

Once we have sourced sufficient high value items we will then partner with Bidora (NZ's equivalent of Vendix) to launch the auction. The proceeds from each auction will benefit up to 6 charities. The auctions will be promoted through Bidora, through PR, and through the communications channels of the benefiting charities, reaching a wider audience than would be possible if just one charity was holding an auction and therefore resulting in more competitive bidding and higher returns for the charities.

We need a web site that we can point potential donors of auction items to, that gives them confidence in BrightLot. We will also leverage the web site with journalists. And of course, charities who are wondering whether or not to use BrightLot will come to our web site and check out our credentials. The tone of the site needs to be warm, friendly, approachable.

We are not locked into the blue and orange colors of the logo and in fact are experimenting with other colors as we speak.

Please note that what we're looking for is the design for the home page, plus a sub page design.

Target Market(s)

CEOs, corporate social responsibility managers, general managers, business owners, charities, the media

Industry/Entity Type

Communications

Requirements
Must have
• Video on home page
Newsletter sign up on all pages
Navigation as per the attached PDF example

```html
<!DOCTYPE html>
<html lang="en">
<head>
<meta charset="utf-8">
<title>BrightLot</title>
<link rel="stylesheet" href="https://fonts.googleapis.com/css2?family=Titillium+Web:wght@400;600;700&display=swap">
<style>
:root{
  --yellow:#f2b705;
  --ink:#1c1c1c;
  --sidebar:#2f2f2f;
  --sidebar-line:#3c3c3c;
  --nav-blue:#5aa8c8;
  --tab-dark:#141414;
  --panel-dark:rgba(20,20,20,.82);
  --red:#d0242b;
  --white:#ffffff;
  --field:#fbf6df;
}
*{box-sizing:border-box;margin:0;padding:0}
html,body{width:1200px;height:714px;overflow:hidden}
body{font-family:"Titillium Web",sans-serif;background:#777;position:relative}
.hero-backdrop{position:absolute;left:0;top:0;width:1200px;height:558px;
  background:linear-gradient(135deg,#5a5a5a 0%,#9a9a9a 25%,#4a4a4a 45%,#b0b0b0 65%,#555 85%,#888 100%)}
.hero-backdrop .tile{position:absolute;background:linear-gradient(160deg,#cfcfcf,#6a6a6a)}
.sidebar{position:absolute;left:199px;top:0;width:182px;height:558px;background:var(--sidebar)}
.brand-box{height:134px;background:var(--yellow);display:flex;align-items:center;justify-content:center}
.brand{display:flex;align-items:center;gap:7px;font-weight:700;font-size:30px;color:var(--ink);line-height:1}
.brand-mark{width:14px;height:14px;border-radius:50%;background:var(--ink)}
.sidebar-stripe{height:8px;background:#222}
.main-nav a{display:block;text-align:right;padding-right:20px;font-weight:600;font-size:13px;text-decoration:none;color:var(--nav-blue);height:31px;line-height:31px;border-bottom:1px solid var(--sidebar-line)}
.main-nav a.active{background:var(--yellow);color:var(--white);height:26px;line-height:26px;font-size:14px;margin-bottom:6px;border:0}
.tabs{position:absolute;top:78px;left:396px;display:flex;gap:14px}
.tab{width:128px;height:32px;background:linear-gradient(#2a2a2a,var(--tab-dark));border:1px solid #444;color:var(--white);font-size:16px;display:flex;align-items:center;justify-content:center}
.video{position:absolute;left:394px;top:125px;width:416px;height:280px;background:#1a1a1a}
.video-frame{height:238px;background:linear-gradient(90deg,#a67a3c 0%,#d9b070 40%,#6f8fb8 65%,#c8a060 85%,#8a6030 100%)}
.play{position:absolute;left:183px;top:108px;width:50px;height:36px;border-radius:8px;background:#1b1b1b;display:flex;align-items:center;justify-content:center}
.progress{position:absolute;left:0;top:246px;width:416px;height:5px;background:var(--red)}
.controls{position:absolute;left:0;top:254px;width:416px;height:26px;display:flex;align-items:center;padding:0 12px;color:#ddd;font-size:9px;gap:10px}
.controls .spacer{flex:1}
.quote{position:absolute;left:381px;top:405px;width:512px;height:153px;background:var(--panel-dark);padding:22px 21px}
.quote h2{color:var(--yellow);font-size:24px;font-weight:600;line-height:1;margin-bottom:4px}
.quote p{width:424px;color:#e8e8e8;font-size:12.4px;line-height:14.3px}
.subscribe{position:absolute;left:822px;top:76px;width:170px}
.subscribe-head{height:40px;background:linear-gradient(#2a2a2a,#0d0d0d);border-radius:6px 6px 0 0;color:var(--white);font-weight:700;font-size:18px;text-align:center;line-height:42px}
.subscribe-body{background:var(--yellow)}
.subscribe-text{padding:7px 10px 0;color:#8a6a00;font-size:10px;line-height:11px;text-align:center}
.field-label{display:block;text-align:center;font-size:12px;color:#4a3a00;margin-top:6px}
.field{display:block;margin:3px auto 0;width:137px;height:22px;border:0;border-radius:2px;background:var(--field)}
.subscribe svg{display:block}
.footer{position:absolute;left:0;top:558px;width:1200px;height:156px;background:var(--yellow)}
.footer-brand{position:absolute;left:199px;top:56px}
.footer-brand .brand{font-size:28px}
.footer h3{font-size:18px;font-weight:600;color:var(--ink);line-height:1}
.footer-col{position:absolute;top:18px}
.footer-col p{color:var(--white);font-size:9px;line-height:14.8px;margin-top:10px}
.tweets{left:422px}
.connect{left:693px}
.contact{left:902px}
.social{display:flex;gap:10px;margin-top:12px;margin-left:3px}
.social span{width:30px;height:30px;border-radius:50%;background:var(--white);color:var(--ink);font-size:6.5px;font-weight:600;display:flex;align-items:center;justify-content:center}
.copyright{position:absolute;left:0;width:1200px;top:133px;text-align:center;color:var(--white);font-size:11px}
</style>
</head>
<body>
<div class="hero-backdrop" role="img" aria-label="Black and white collage of sports memorabilia, event tickets, a stadium and a cruise ship">
  <div class="tile" style="left:0;top:0;width:199px;height:176px"></div>
  <div class="tile" style="left:0;top:362px;width:199px;height:190px"></div>
  <div class="tile" style="left:892px;top:0;width:226px;height:176px"></div>
  <div class="tile" style="left:992px;top:362px;width:126px;height:190px"></div>
</div>

<aside class="sidebar">
  <div class="brand-box">
    <div class="brand"><span class="brand-mark"></span>BrightLot</div>
  </div>
  <div class="sidebar-stripe"></div>
  <nav class="main-nav">
    <a class="active" href="#">HOME</a>
    <a href="#">HOW IT WORKS</a>
    <a href="#">ACT OF GOODNESS</a>
    <a href="#">GOODNESS PARTNERST</a>
    <a href="#">ABOUT</a>
    <a href="#">CONTACT</a>
  </nav>
</aside>

<nav class="tabs">
  <a class="tab">Donors</a>
  <a class="tab">Charities</a>
  <a class="tab">Auctions</a>
</nav>

<section class="video">
  <div class="video-frame" role="img" aria-label="Video still of a luxury cruise cabin with a bed and ocean view"></div>
  <div class="play"><svg width="16" height="16" viewBox="0 0 16 16"><path d="M3 1 L14 8 L3 15 Z" fill="#fff"/></svg></div>
  <div class="progress"></div>
  <div class="controls">
    <svg width="14" height="12" viewBox="0 0 14 12"><path d="M1 4h3l4-3v10l-4-3H1z" fill="#aaa"/><path d="M10 3q2 3 0 6" stroke="#aaa" fill="none"/></svg>
    <span>0:00</span>
    <span class="spacer"></span>
    <svg width="9" height="9" viewBox="0 0 9 9"><circle cx="4.5" cy="4.5" r="4" fill="#aaa"/></svg>
    <span>ClipView</span>
    <svg width="12" height="12" viewBox="0 0 12 12" fill="none" stroke="#ccc"><path d="M1 4V1h3M8 1h3v3M11 8v3H8M4 11H1V8"/></svg>
  </div>
</section>

<section class="quote">
  <h2>QUOTE</h2>
  <p>Lorem ipsum dolor sit amet, consectetuer adipiscing elit, sed diam nonummy nibh euismod tincidunt ut laoreet dolore magna aliquam erat volutpat. Ut wisi enim ad minim veniam, quis nostrud exerci tation ullamcorper suscipit lobortis nisl ut aliquip ex ea commodo consequat. Duis autem vel eum iriure dolor in hendrerit in vulputate velit esse molestie consequat, vel illum dolore eu feugiat nulla facilisis .</p>
</section>

<section class="subscribe">
  <div class="subscribe-head">SUSCRIBE</div>
  <div class="subscribe-body">
    <p class="subscribe-text">Charity auctions are a great way to get luxury items and unique experiences while helping a worthwhile cause. Subscribe to our email list to be kept informed about upcoming auctions.</p>
    <label class="field-label">First Name:</label><input class="field">
    <label class="field-label">Last Name:</label><input class="field">
    <label class="field-label">City Town:</label><input class="field">
    <label class="field-label">Email Adderess:</label><input class="field">
    <div style="height:10px"></div>
  </div>
  <svg width="170" height="26" viewBox="0 0 170 26"><path d="M0 0H170V10L85 26L0 10Z" fill="#f2b705"/></svg>
</section>

<footer class="footer">
  <div class="footer-brand">
    <div class="brand"><span class="brand-mark"></span>BrightLot</div>
  </div>
  <div class="footer-col tweets">
    <h3>Latest Tweets</h3>
    <p>@MARA7<br>Checkout my top #smallbiz tip featured in<br>@SmallDeskMag on how to reduce<br>#business stress http://lnk.ex/a8Kq2<br>http://lnk.ex/r4Tz9</p>
  </div>
  <div class="footer-col connect">
    <h3>Stay Connected</h3>
    <div class="social"><span>Chirpr</span><span>Friendlink</span><span>Feed</span></div>
  </div>
  <div class="footer-col contact">
    <h3>Contact us</h3>
    <p>58 Harbour Lane<br>Suite 12<br>Wellington 6011<br>Phone : 555-014-2290</p>
  </div>
  <div class="copyright">BRIGHTLOT © 2013 | All Rights Reserved &nbsp;| PrivacyPolicy</div>
</footer>
</body>
</html>
```